WP website design for Pelton

We need a wordpress design that will incorporate a professional color scheme with company logo in a clean layout. The design needs to consider that this will be developed on a responsive theme. Colors are will be the green of the logo and any others that will creatively highlight it.

Industry/Entity Type

It Company

Font styles to use
Sans Serif

Requirements
Must have
• Navigation: 1) Home 2) Auctions 3) Auction Services 4) Sellers 5) RK Pelton Livestock 6) About Us 7) Contact Us
Site will have slideshow element, image attached.
Widgets will be: 1)Email Signup form 2) Featured Auctions widget 3) Social Media (Chirply, Vidloop, RSS) 4) News & Events blog
Footer will have smaller company logo, association logos (attached) and contact info (below)
▪ R.K. Pelton Inc. / Auctioneers
▪ 4716 NC Hwy 91
▪ Marbury, NC 27604
▪ Office: (252) 555-0184
▪ Cell: (252) 555-0137
▪ email: rkpelton@rkpelton-example.com
Nice to have
• Site will have drop-down menus - please indicate the styling, for instance the dropdown menus

```html
<!DOCTYPE html>
<html lang="en">
<head>
<meta charset="utf-8">
<title>R.K. Pelton Inc. / Auctioneers</title>
<link href="https://fonts.googleapis.com/css2?family=Cinzel:wght@400;700&family=Roboto:wght@300;400;500;700&family=Arimo:wght@400;700&display=swap" rel="stylesheet">
<style>
  :root {
    --green: #2f8a1c;
    --green-dark: #1f6b10;
    --green-band: #3f9a22;
    --green-band-light: #4aa82a;
    --orange: #f07a14;
    --orange-dark: #e0650a;
    --ink: #222;
    --text: #333;
    --muted: #777;
    --line: #d8d8d8;
    --field-bg: #e9e9e9;
    --white: #fff;
    --map-tone: #d6e6d3;
    --pasture-tone: #b9c48e;
    --landscape-top: #b9d6ee;
    --landscape-bottom: #c49a5a;
    --meadow-tone: #8fae4e;
  }
  * { box-sizing: border-box; margin: 0; padding: 0; }
  html, body { width: 1200px; height: 947px; overflow: hidden; background: var(--white); }
  body { position: relative; font-family: "Roboto", sans-serif; color: var(--text); }

  /* Header */
  .brand {
    position: absolute; left: 118px; top: 38px;
    display: flex; align-items: center; gap: 14px;
    color: var(--green); font-family: "Cinzel", serif; font-weight: 700; white-space: nowrap;
  }
  .brand-mark { width: 46px; height: 46px; border-radius: 50%; background: var(--green); flex: none; }
  .brand-name { font-size: 25px; line-height: 1.1; }
  .brand-name small { display: block; font-size: 17px; margin-top: 3px; }

  .call { position: absolute; left: 651px; top: 45px; display: flex; align-items: center; gap: 10px; }
  .call-icon { width: 44px; height: 44px; }
  .call-label { font-family: "Roboto", sans-serif; font-size: 15px; color: #444; display: block; margin-bottom: -2px; }
  .call-number { font-family: "Cinzel", serif; font-size: 25px; color: var(--orange); letter-spacing: .5px; }

  .newsletter-btn {
    position: absolute; left: 903px; top: 40px; width: 231px; height: 56px;
    background: linear-gradient(#fb8c26, var(--orange-dark));
    border: 1px solid #d45f08; border-radius: 4px;
    box-shadow: 0 2px 3px rgba(0,0,0,.2);
    display: flex; align-items: center; justify-content: center; gap: 12px;
    color: var(--white); font-family: "Cinzel", serif; font-weight: 700; font-size: 15px; letter-spacing: .5px;
  }

  /* Navigation */
  .main-nav {
    position: absolute; left: 95px; top: 142px; width: 1045px; height: 48px;
    border: 1px solid var(--line); border-radius: 8px; background: var(--white);
    display: flex; align-items: stretch; overflow: hidden;
  }
  .main-nav a {
    display: flex; align-items: center; justify-content: center;
    font-family: "Arimo", sans-serif; font-size: 13px; color: #111; text-decoration: none;
    border-right: 1px solid var(--line);
  }
  .main-nav a.active { background: var(--green); color: var(--white); border-radius: 7px 0 0 7px; }
  .search { margin-left: auto; display: flex; align-items: center; padding-right: 13px; }
  .search-field {
    width: 156px; height: 28px; background: var(--field-bg); border-radius: 3px 0 0 3px;
    font-family: "Roboto", sans-serif; font-size: 14px; color: #777; padding: 6px 24px;
  }
  .search-btn { width: 35px; height: 28px; background: var(--green); display: flex; align-items: center; justify-content: center; border-radius: 0 3px 3px 0; }

  /* Hero slideshow */
  .hero {
    position: absolute; left: 0; top: 196px; width: 1200px; height: 458px;
    background: linear-gradient(var(--green-band-light), var(--green-band));
  }
  .slide { position: absolute; border-radius: 5px; border: 1px solid rgba(255,255,255,.6); }
  .slide-side-left { left: 95px; top: 54px; width: 150px; height: 324px; background: var(--map-tone); }
  .slide-side-right { left: 980px; top: 54px; width: 156px; height: 324px; background: var(--pasture-tone); }
  .slide-main {
    left: 218px; top: 34px; width: 791px; height: 353px; z-index: 2;
    background: linear-gradient(var(--landscape-top), var(--landscape-bottom));
  }
  .slide-shadow { position: absolute; left: 330px; top: 368px; z-index: 1; }
  .slide-dots { position: absolute; left: 562px; top: 421px; display: flex; gap: 5px; align-items: center; }
  .dot { width: 16px; height: 16px; border-radius: 50%; background: radial-gradient(circle at 40% 35%, #fff, #bbb); box-shadow: 0 1px 2px rgba(0,0,0,.4); }
  .dot.current { width: 19px; height: 19px; background: radial-gradient(circle at 40% 35%, #ffab55, var(--orange-dark)); }

  /* Welcome */
  .section-title { font-family: "Cinzel", serif; font-size: 22px; font-weight: 700; letter-spacing: .5px; color: var(--ink); white-space: nowrap; }
  .welcome-title { position: absolute; left: 100px; top: 687px; }
  .welcome-title span { color: var(--green); font-weight: 400; }
  .welcome-photo {
    position: absolute; left: 100px; top: 735px; width: 190px; height: 199px;
    border: 3px solid var(--green);
    background: var(--meadow-tone);
  }
  .welcome-copy { position: absolute; left: 303px; top: 733px; width: 400px; font-size: 14.5px; line-height: 24px; font-weight: 300; color: #333; }
  .welcome-copy p + p { margin-top: 22px; }
  .read-more {
    position: absolute; left: 303px; top: 914px; width: 121px; height: 36px;
    border: 1px solid #bbb; border-radius: 4px; background: linear-gradient(#fff, #ddd);
    font-family: "Arimo", sans-serif; font-size: 14px; color: #222; text-align: center; line-height: 34px;
  }

  /* Newsletter subscription */
  .subscribe-title { position: absolute; left: 754px; top: 687px; }
  .subscribe-title span { color: var(--orange); font-weight: 400; }
  .subscribe-note { position: absolute; left: 753px; top: 722px; width: 360px; font-family: "Arimo", sans-serif; font-size: 12px; line-height: 19px; color: var(--muted); }
  .field {
    position: absolute; left: 754px; width: 366px; height: 47px;
    border: 1px solid var(--line); border-radius: 8px; display: flex; align-items: center; overflow: hidden;
    font-family: "Arimo", sans-serif; font-size: 14px;
  }
  .field-icon { width: 46px; height: 100%; display: flex; align-items: center; justify-content: center; margin-right: 15px; }
  .field-name { top: 782px; color: #222; }
  .field-name .field-icon { background: var(--green-dark); }
  .field-email { top: 841px; color: var(--orange-dark); }
  .field-email .field-icon { background: var(--orange-dark); }
  .signup-btn {
    position: absolute; left: 937px; top: 904px; width: 183px; height: 45px;
    background: linear-gradient(#2a7c12, #1b5e0a); border-radius: 4px 4px 0 0;
    color: var(--white); font-family: "Arimo", sans-serif; font-size: 20px; text-align: center; line-height: 45px;
  }
</style>
</head>
<body>
  <header>
    <div class="brand">
      <span class="brand-mark"></span>
      <span class="brand-name">R.K. Pelton<small>Inc. / Auctioneers</small></span>
    </div>

    <div class="call">
      <svg class="call-icon" viewBox="0 0 44 44" aria-hidden="true">
        <circle cx="22" cy="22" r="20" fill="none" stroke="#2f8a1c" stroke-width="2.5"/>
        <path d="M15 11c2-1 3 0 4 2l2 4c0 2-2 2-2 3 1 3 3 5 5 6 1 0 1-2 3-2l4 2c2 1 3 2 2 4-1 2-3 3-5 3-8-1-15-8-16-16 0-3 1-5 3-6z" fill="#2f8a1c"/>
      </svg>
      <div>
        <span class="call-label">Call Us Now</span>
        <span class="call-number">(252) 555-0137</span>
      </div>
    </div>

    <div class="newsletter-btn">
      <svg width="30" height="18" viewBox="0 0 30 18" aria-hidden="true">
        <rect x="1" y="1" width="28" height="16" fill="none" stroke="#fff" stroke-width="2"/>
        <path d="M1 1l14 10 14-10" fill="none" stroke="#fff" stroke-width="2"/>
      </svg>
      Newsletter signup
    </div>
  </header>

  <nav class="main-nav">
    <a class="active" href="#" style="width:103px">HOME</a>
    <a href="#" style="width:91px">AUCTIONS</a>
    <a href="#" style="width:159px">AUCTION SERVICES</a>
    <a href="#" style="width:96px">SELLERS</a>
    <a href="#" style="width:171px">RK PELTON LIVESTOCK</a>
    <a href="#" style="width:96px">ABOUT US</a>
    <a href="#" style="width:110px">CONTACT US</a>
    <div class="search">
      <div class="search-field">Search</div>
      <div class="search-btn">
        <svg width="16" height="16" viewBox="0 0 16 16" aria-hidden="true">
          <circle cx="6.5" cy="6.5" r="4.5" fill="none" stroke="#fff" stroke-width="2"/>
          <path d="M10 10l4.5 4.5" stroke="#fff" stroke-width="2.5" stroke-linecap="round"/>
        </svg>
      </div>
    </div>
  </nav>

  <section class="hero">
    <div class="slide slide-side-left" role="img" aria-label="Map of the North Carolina coast"></div>
    <div class="slide slide-side-right" role="img" aria-label="Cattle grazing on a pasture"></div>
    <svg class="slide-shadow" width="570" height="40" aria-hidden="true">
      <ellipse cx="285" cy="12" rx="285" ry="18" fill="rgba(0,40,0,.45)"/>
    </svg>
    <div class="slide slide-main" role="img" aria-label="Autumn farmland beside a still pond"></div>
    <div class="slide-dots">
      <span class="dot"></span><span class="dot"></span><span class="dot current"></span><span class="dot"></span><span class="dot"></span>
    </div>
  </section>

  <main>
    <h2 class="section-title welcome-title">Welcome to <span>R.K. Pelton Inc. / Auctioneers</span></h2>
    <div class="welcome-photo" role="img" aria-label="Cattle standing in a flowering field"></div>
    <div class="welcome-copy">
      <p>Lorem Ipsum is simply dummy text of the printing and type-setting industry.</p>
      <p>Lorem Ipsum has been the industry's standard dummy text ever since the 1500s, when an unknown printer took a galley of type and scrambled it to make a type specimen book. It has survived not only five centuries.</p>
    </div>
    <div class="read-more">READ MORE</div>

    <h2 class="section-title subscribe-title"><span>Newsletter</span> Subscription</h2>
    <p class="subscribe-note">Subscribe for our FREE Newsletter to get updates on latest auctions on North Carolina Livestocks.</p>
    <div class="field field-name">
      <span class="field-icon">
        <svg width="16" height="16" viewBox="0 0 16 16" aria-hidden="true">
          <circle cx="8" cy="4.5" r="3.5" fill="#111"/>
          <path d="M1 16c0-5 3-7 7-7s7 2 7 7z" fill="#111"/>
        </svg>
      </span>Name
    </div>
    <div class="field field-email">
      <span class="field-icon">
        <svg width="18" height="13" viewBox="0 0 18 13" aria-hidden="true">
          <rect x="0" y="0" width="18" height="13" fill="#6a2a06"/>
          <path d="M0 0l9 7 9-7" fill="none" stroke="#e0650a" stroke-width="1.5"/>
        </svg>
      </span>Email
    </div>
    <div class="signup-btn">SIGNUP NOW!</div>
  </main>
</body>
</html>
```